Outstanding but small benefit administration firm serving large clients needs a website redesign

While the content on our current website is fine, when people arrive at our website, they know immediately that it was designed years ago. We are looking for something that can potentially be maintained on a content management system because we would like to hire a google certified expert to help with adwords and they often want to change the website or add meta data. We want the design to be mobile device friendly.

As for our company, we stress data accuracy, client customization and outstanding customer service. All of our competitors are large corporations (Corvellan, Tolbin, Qualix, PerkWaypoint, etc.). When we get a client, they stay with us. So many of our competitors do a horrible job with administration that many companies just think that's the way it is in this industry. We need to change that thinking! There is someone who can do it right at a reasonable price. We have very few out of scope fees. RMT knows how to make the transition from one administrator to us as painless as possible.

We like our current colors. We don't have a lot of time to write additional content.

Target Market(s)

Companies with 5,000 to 50,000 employees

Coding

Coded - Design and coding required

Number of Pages Required

2 page

Font styles to use
Sans Serif

Requirements
Must have
• If everything doesn't fit on one page, please show me what the second page would look like. For example, if there are See More links, what happens?
• We need for people to be able to submit short contact us with their company name as a required field.
• Ideally this website will be put on wordpress or something similar.
• Must be mobile device friendly.
Should not have
• Login, Register, Maps of our location, website search

```html
<!DOCTYPE html>
<html lang="en">
<head>
<meta charset="utf-8">
<title>Ridgeway Member Trust</title>
<link rel="stylesheet" href="https://fonts.googleapis.com/css2?family=Arimo:wght@400;700&family=Open+Sans:ital,wght@0,400;0,600;0,700;1,400&display=swap">
<style>
:root{
  --green:#8cc63f;
  --green-dark:#6fae2a;
  --blue:#3daee9;
  --ink:#222427;
  --text:#6b6f73;
  --line:#e3e5e8;
  --footer:#2b2f34;
  --footer-line:#3b4046;
  --white:#ffffff;
}
*{box-sizing:border-box;margin:0;padding:0}
html,body{width:1200px;height:2466px;overflow:hidden}
body{background:var(--white);font-family:"Open Sans",Arial,sans-serif;color:var(--text);position:relative}
.abs{position:absolute}

/* header */
.topbar{position:absolute;left:0;top:0;width:1200px;height:4px;background:linear-gradient(90deg,var(--green),var(--blue))}
.site-header{position:absolute;left:0;top:4px;width:1200px;height:78px}
.brand{position:absolute;left:88px;top:20px;display:flex;align-items:center;gap:12px}
.brand-dot{width:26px;height:26px;border-radius:50%;background:var(--blue)}
.brand-name{font-family:"Arimo",Arial,sans-serif;font-size:26px;color:#555a5f;letter-spacing:-.2px}
.main-nav{position:absolute;right:202px;top:31px;display:flex;gap:16px;font-family:"Arimo",Arial,sans-serif;font-weight:700;font-size:13px;color:var(--ink);white-space:nowrap}
.main-nav .active{color:var(--green)}
.head-icon{position:absolute;top:22px;width:38px;height:38px;border-radius:50%;border:2px solid;display:flex;align-items:center;justify-content:center}
.head-icon.mail{left:1015px;border-color:var(--blue)}
.head-icon.call{left:1062px;border-color:var(--green)}

/* hero */
.hero{position:absolute;left:0;top:82px;width:1200px;height:444px;background:linear-gradient(100deg,#d9dcd8 0%,#b9a79a 25%,#e8e4df 45%,#9fb0c4 70%,#5d6a78 100%)}
.hero-title{position:absolute;left:0;width:1200px;top:270px;text-align:center;font-family:"Arimo",Arial,sans-serif;font-weight:700;font-size:46px;color:var(--white);text-shadow:0 2px 6px rgba(0,0,0,.45)}
.slider-dots{position:absolute;top:465px;left:510px;display:flex;gap:4px}
.slider-dots span{width:32px;height:5px;border-radius:3px;background:var(--white)}
.slider-dots .on{background:var(--green)}

/* section badge */
.badge{position:absolute;width:72px;height:72px;border-radius:50%;background:var(--white);box-shadow:0 2px 6px rgba(0,0,0,.15);display:flex;align-items:center;justify-content:center}
.badge span{width:22px;height:22px;border-radius:50%;background:var(--blue)}

/* welcome */
.welcome-title{position:absolute;top:572px;left:0;width:1200px;text-align:center;font-family:"Arimo",Arial,sans-serif;font-weight:700;font-size:24px;color:var(--ink)}
.welcome-text{position:absolute;top:622px;left:190px;width:820px;text-align:center;font-size:13.5px;line-height:26px}
.service-card{position:absolute;top:743px;width:320px;height:364px;background:var(--white);box-shadow:0 1px 5px rgba(0,0,0,.18);border-bottom:4px solid var(--green)}
.service-card.blue{border-bottom-color:var(--blue)}
.card-photo{height:181px}
.card-title{margin-top:24px;text-align:center;font-family:"Arimo",Arial,sans-serif;font-weight:700;font-size:18px;color:var(--ink)}
.card-text{margin:14px 28px 0;text-align:center;font-size:12.5px;line-height:23px;height:69px;overflow:hidden}
.read-more{display:block;margin-top:18px;text-align:center;font-weight:700;font-size:12.5px;color:var(--green)}
.read-more.blue{color:var(--blue)}

/* technology */
.tech{position:absolute;left:0;top:1179px;width:1200px;height:446px;background:linear-gradient(180deg,#3e5a7c 0%,#6f88a6 45%,#4a6686 75%,#2f4a6b 100%)}
.tech-title{position:absolute;top:1225px;left:0;width:1200px;text-align:center;font-family:"Arimo",Arial,sans-serif;font-weight:700;font-size:24px;color:var(--white)}
.tech-text{position:absolute;top:1267px;left:230px;width:740px;text-align:center;font-size:13.5px;line-height:25px;color:var(--white)}
.tech-box{position:absolute;top:1381px;width:191px;height:197px;background:rgba(236,240,244,.92);text-align:center;padding-top:56px}
.tech-icon{position:absolute;top:-42px;left:54px;width:84px;height:84px;border-radius:50%;background:var(--blue);border:4px solid var(--white);display:flex;align-items:center;justify-content:center}
.tech-box h3{font-family:"Arimo",Arial,sans-serif;font-weight:700;font-size:17px;color:var(--ink)}
.tech-box p{margin:10px 10px 0;font-size:12px;line-height:20px;height:60px;overflow:hidden}
.tech-box .read-more{margin-top:10px}

/* info columns */
.col-head{position:absolute;top:1660px;display:flex;align-items:center;gap:8px;font-family:"Arimo",Arial,sans-serif;font-weight:700;font-size:24px;color:var(--ink)}
.col-head i{width:14px;height:14px;border-radius:50%;background:var(--blue);display:block;margin-top:-14px}
.why-list{position:absolute;left:99px;top:1730px;width:320px;list-style:none}
.why-list li{position:relative;padding-left:24px;font-size:12.5px;line-height:20px;margin-bottom:14px}
.why-list li::before{content:"";position:absolute;left:0;top:3px;width:14px;height:14px;border-radius:50%;background:var(--blue)}
.why-list li::after{content:"";position:absolute;left:4px;top:6px;width:5px;height:3px;border-left:2px solid #fff;border-bottom:2px solid #fff;transform:rotate(-45deg)}
.case-photo{position:absolute;left:441px;top:1738px;width:308px;height:150px;background:linear-gradient(135deg,#eef3f8,#b9cde0 55%,#dbe7f1)}
.case-text{position:absolute;left:441px;top:1905px;width:310px;font-size:12px;line-height:23px}
.testimonial{position:absolute;left:795px;top:1746px;width:305px;height:118px;border:1px solid var(--line);background:var(--white);padding:12px 22px}
.testimonial::after{content:"";position:absolute;left:6px;bottom:-9px;width:16px;height:16px;background:var(--white);border-right:1px solid var(--line);border-bottom:1px solid var(--line);transform:rotate(45deg)}
.testimonial q{display:block;font-style:italic;font-size:12px;line-height:22px;color:#555}
.testimonial q em{color:var(--green)}
.t-name{position:absolute;left:822px;top:1868px;font-size:15px;color:var(--ink);font-weight:600}
.t-role{position:absolute;left:833px;top:1889px;font-size:12px;font-style:italic;color:var(--green-dark)}
.slide-arrow{position:absolute;top:1800px;width:20px;height:38px;background:#eceef0;display:flex;align-items:center;justify-content:center}
.client-mark{position:absolute;left:795px;top:1957px;width:188px;height:80px;border:1px solid var(--line);display:flex;align-items:center;justify-content:center;font-family:"Arimo",Arial,sans-serif;font-weight:700;font-size:28px;color:#b51a1f}

/* footer */
.footer{position:absolute;left:0;top:2085px;width:1200px;height:381px;background:var(--footer)}
.footer-stripe{position:absolute;left:0;top:2085px;width:1200px;height:4px;background:linear-gradient(90deg,var(--green),var(--blue))}
.footer-mark{position:absolute;left:150px;top:2140px;width:70px;height:70px;border-radius:50%;background:var(--blue)}
.v-rule{position:absolute;top:2105px;width:1px;height:280px;background:var(--footer-line)}
.foot-title{position:absolute;top:2126px;font-family:"Arimo",Arial,sans-serif;font-weight:700;font-size:14.5px;color:var(--white);letter-spacing:.3px}
.field{position:absolute;height:33px;background:var(--white);font-size:11px;color:#777;padding:9px 10px;line-height:15px}
.submit{position:absolute;left:695px;top:2333px;width:104px;height:39px;background:var(--green);color:var(--white);font-weight:700;font-size:12px;display:flex;align-items:center;justify-content:center}
.info-icon{position:absolute;left:871px;width:38px;height:38px;border-radius:50%;border:2px solid var(--white);display:flex;align-items:center;justify-content:center}
.info-text{position:absolute;left:952px;font-size:12px;line-height:22px;color:var(--white)}
.h-rule{position:absolute;left:99px;top:2397px;width:1002px;height:1px;background:var(--footer-line)}
.copyright{position:absolute;left:99px;top:2420px;font-size:12px;color:#c9ccd0}
.social{position:absolute;top:2413px;display:flex;gap:8px;left:954px}
.social span{width:31px;height:31px;border-radius:50%}
</style>
</head>
<body>

<div class="topbar"></div>
<header class="site-header">
  <div class="brand"><span class="brand-dot"></span><span class="brand-name">Ridgeway Member Trust</span></div>
  <nav class="main-nav">
    <span class="active">HOME</span><span>WHY RMT</span><span>SERVICES</span><span>TECHNOLOGY</span><span>CASE STUDIES</span><span>CONTACT US</span>
  </nav>
  <div class="head-icon mail"><svg width="18" height="14" viewBox="0 0 18 14"><rect x="1" y="1" width="16" height="12" fill="none" stroke="#3daee9" stroke-width="2"/><path d="M1 1l8 7 8-7" fill="none" stroke="#3daee9" stroke-width="2"/></svg></div>
  <div class="head-icon call"><svg width="18" height="18" viewBox="0 0 24 24"><path d="M6.6 10.8a15 15 0 006.6 6.6l2.2-2.2a1 1 0 011-.25 11.4 11.4 0 003.6.57 1 1 0 011 1V20a1 1 0 01-1 1A17 17 0 013 4a1 1 0 011-1h3.5a1 1 0 011 1c0 1.25.2 2.45.57 3.57a1 1 0 01-.25 1z" fill="#8cc63f"/></svg></div>
</header>

<section class="hero" role="img" aria-label="Photo of three colleagues gathered around a laptop in a bright office"></section>
<h1 class="hero-title">RMT is your problem solving partner</h1>
<div class="slider-dots"><span></span><span></span><span class="on"></span><span></span><span></span></div>

<div class="badge" style="left:564px;top:490px"><span></span></div>
<h2 class="welcome-title">WELCOME TO RIDGEWAY MEMBER TRUST</h2>
<p class="welcome-text">Ridgeway Member Trust (RMT) is a boutique organization providing large plan sponsors a customer service model using only trained benefit professionals and a totally customizable, highly flexible technology platform. This unique model allows RMT to provide large company IT capabilities, unparalleled services and very competitive fees.</p>

<article class="service-card" style="left:99px">
  <div class="card-photo" role="img" aria-label="Photo of a team of professionals reviewing documents together" style="background:linear-gradient(135deg,#f2f2f2,#c9c9c9 50%,#e9e9e9)"></div>
  <h3 class="card-title">Health and Welfare Administration</h3>
  <p class="card-text">RMT provides a broad range of health and welfare administration services. In addition to the summary listed below</p>
  <span class="read-more">READ MORE &gt;&gt;</span>
</article>
<article class="service-card blue" style="left:440px">
  <div class="card-photo" role="img" aria-label="Photo of a hand pointing at charts on a tablet" style="background:linear-gradient(135deg,#eaf1f7,#a9c6dd 55%,#e4ecf2)"></div>
  <h3 class="card-title">Defined Benefit Administration</h3>
  <p class="card-text">RMT provides a comprehensive set of defined benefit and non-qualified SERP administration services. We are often successful</p>
  <span class="read-more blue">READ MORE &gt;&gt;</span>
</article>
<article class="service-card" style="left:781px">
  <div class="card-photo" role="img" aria-label="Photo of a business team meeting around a table" style="background:linear-gradient(135deg,#f4f1ee,#cdbfb3 50%,#ebe7e3)"></div>
  <h3 class="card-title">Consulting Services</h3>
  <p class="card-text">RMT provides high level consulting services. Our principals represent some of the most senior consulting expertise in the industry.</p>
  <span class="read-more">READ MORE &gt;&gt;</span>
</article>

<section class="tech" role="img" aria-label="Photo of a glass office building seen from below, tinted blue"></section>
<div class="badge" style="left:564px;top:1143px"><span></span></div>
<h2 class="tech-title">OUR TECHNOLOGY</h2>
<p class="tech-text">RMT has proportionally one of the largest IT staffs in the industry. Our systems are more sophisticated and user friendly than our larger competitors. Most of our systems are built and maintained in-house.</p>

<div class="tech-box" style="left:99px">
  <div class="tech-icon"><svg width="36" height="36" viewBox="0 0 36 36" fill="none" stroke="#fff" stroke-width="2.5"><circle cx="18" cy="18" r="14"/><ellipse cx="18" cy="18" rx="6" ry="14"/><path d="M4 18h28M7 10h22M7 26h22"/></svg></div>
  <h3>WEB SERVICES</h3><p>RMT has a flexible and extendable web application for benefit administration.</p><span class="read-more">READ MORE &gt;&gt;</span>
</div>
<div class="tech-box" style="left:302px">
  <div class="tech-icon"><svg width="24" height="36" viewBox="0 0 24 36" fill="none" stroke="#fff" stroke-width="2.5"><rect x="2" y="2" width="20" height="32" rx="3"/><path d="M2 27h20"/><circle cx="12" cy="31" r="1" fill="#fff"/></svg></div>
  <h3>PHONE SERVICES</h3><p>RMT has a sophisticated phone system in which calls are recorded for training</p><span class="read-more">READ MORE &gt;&gt;</span>
</div>
<div class="tech-box" style="left:505px">
  <div class="tech-icon"><svg width="38" height="38" viewBox="0 0 38 38" fill="none" stroke="#fff" stroke-width="3"><circle cx="14" cy="20" r="6"/><circle cx="14" cy="20" r="11" stroke-dasharray="4 3"/><circle cx="29" cy="9" r="3"/><circle cx="29" cy="9" r="6" stroke-dasharray="3 2" stroke-width="2"/></svg></div>
  <h3>VENDOR FEEDS</h3><p>RMT currently feeds or receives feeds from almost 100 different vendors.</p><span class="read-more">READ MORE &gt;&gt;</span>
</div>
<div class="tech-box" style="left:708px">
  <div class="tech-icon"><svg width="28" height="36" viewBox="0 0 28 36" fill="none" stroke="#fff" stroke-width="2.5"><path d="M2 2h16l8 8v24H2z"/><path d="M18 2v8h8M7 17h14M7 23h14M7 29h10"/></svg></div>
  <h3>REPORTING</h3><p>RMT offers its clients a variety of reporting options, including customized participant</p><span class="read-more">READ MORE &gt;&gt;</span>
</div>
<div class="tech-box" style="left:910px">
  <div class="tech-icon"><svg width="34" height="34" viewBox="0 0 34 34"><path d="M24 2a8 8 0 00-7.6 10.4L3 25.8a3 3 0 004.2 4.2l13.4-13.4A8 8 0 0032 10l-5 3-4-1-1-4 3-5z" fill="#fff"/></svg></div>
  <h3>TOOLS</h3><p>RMT uses the most current and sophisticated tools to develop its software</p><span class="read-more">READ MORE &gt;&gt;</span>
</div>

<h2 class="col-head" style="left:99px"><i></i>WHY RMT</h2>
<ul class="why-list">
  <li>The benefits outsourcing industry is going through challenging times.</li>
  <li>RMT is systemically structured to address these issues.</li>
  <li>Clients are asked to limit the complexity of plans offered and restrict customization</li>
  <li>RMT specializes in highly complex plan structures and challenging populations.</li>
  <li>Our target market ranges from 5,000 to 50,000 participants per client.</li>
</ul>
<span class="read-more abs" style="left:99px;top:2015px;margin:0">READ MORE &gt;&gt;</span>

<h2 class="col-head" style="left:433px"><i></i>CASE STUDIES</h2>
<div class="case-photo" role="img" aria-label="Illustration of a glass globe on a blue office background"></div>
<p class="case-text">A global leader in the development and manufacture of automotive safety systems came to RMT for assistance. The company is a conglomeration of many different companies that have merged over the years,</p>
<span class="read-more abs" style="left:441px;top:2015px;margin:0">READ MORE &gt;&gt;</span>

<h2 class="col-head" style="left:785px"><i></i>TESTIMONIALS</h2>
<div class="slide-arrow" style="left:783px"><svg width="8" height="12" viewBox="0 0 8 12"><path d="M7 1L2 6l5 5" fill="none" stroke="#999" stroke-width="2"/></svg></div>
<div class="slide-arrow" style="left:1094px"><svg width="8" height="12" viewBox="0 0 8 12"><path d="M1 1l5 5-5 5" fill="none" stroke="#999" stroke-width="2"/></svg></div>
<blockquote class="testimonial"><q>RMT has been our vendor from their inception. They handle our most complex plans with a seemingly infinite amount of patience and professionalism. <em>Read More &gt;&gt;</em></q></blockquote>
<div class="t-name">- Dana Relko</div>
<div class="t-role">Vice President, Compensation and Benefits</div>
<div class="client-mark">Vantrel</div>

<footer class="footer"></footer>
<div class="footer-stripe"></div>
<div class="footer-mark"></div>
<div class="v-rule" style="left:307px"></div>
<div class="v-rule" style="left:833px"></div>

<h3 class="foot-title" style="left:339px">CONTACT FORM</h3>
<div class="field" style="left:339px;top:2167px;width:225px">NAME :</div>
<div class="field" style="left:574px;top:2167px;width:225px">COMPANY :</div>
<div class="field" style="left:339px;top:2212px;width:225px">EMAIL :</div>
<div class="field" style="left:574px;top:2212px;width:225px">PHONE :</div>
<div class="field" style="left:339px;top:2256px;width:460px;height:66px">MESSAGE :</div>
<div class="submit">SUBMIT</div>

<h3 class="foot-title" style="left:871px">CONTACT INFORMATION</h3>
<div class="info-icon" style="top:2179px"><svg width="14" height="18" viewBox="0 0 14 18"><path d="M7 1a6 6 0 00-6 6c0 4.5 6 10 6 10s6-5.5 6-10a6 6 0 00-6-6z" fill="none" stroke="#fff" stroke-width="1.8"/><circle cx="7" cy="7" r="2" fill="#fff"/></svg></div>
<div class="info-text" style="top:2176px">2210 Alder Ridge Rd<br>Lakeview Twp., MI 48000</div>
<div class="info-icon" style="top:2245px"><svg width="16" height="16" viewBox="0 0 24 24"><path d="M6.6 10.8a15 15 0 006.6 6.6l2.2-2.2a1 1 0 011-.25 11.4 11.4 0 003.6.57 1 1 0 011 1V20a1 1 0 01-1 1A17 17 0 013 4a1 1 0 011-1h3.5a1 1 0 011 1c0 1.25.2 2.450.57 3.57a1 1 0 01-.25 1z" fill="#fff"/></svg></div>
<div class="info-text" style="top:2253px">555-014-2271</div>
<div class="info-icon" style="top:2314px"><svg width="18" height="16" viewBox="0 0 18 16" fill="none" stroke="#fff" stroke-width="1.6"><rect x="1" y="5" width="16" height="10" rx="1"/><path d="M4 5V1h10v4"/><path d="M5 9h2M9 9h2M13 9h1M5 12h2M9 12h2"/></svg></div>
<div class="info-text" style="top:2322px">555-014-2284</div>

<div class="h-rule"></div>
<p class="copyright">© 2016, Ridgeway Member Trust. All Rights Reserved.</p>
<div class="social" aria-label="Social links">
  <span style="background:#3b5998"></span><span style="background:#1da1f2"></span><span style="background:#dd4b39"></span><span style="background:#b3222a"></span>
</div>

</body>
</html>
```